Income Tax Flyer - Updates Needed

Just need to update this flyer design and give it a new look. We would like to keep all the same wording but make it stand out a little more. Our selling point is the "Same Day Tax Advance up to $6,000"

Industry/Entity Type

Lending, Small Loans, Tax Services, Title Loans, Personal Loans

```html
<!DOCTYPE html>
<html lang="en">
<head>
<meta charset="utf-8">
<title>Tax Advance Flyer</title>
<link href="https://fonts.googleapis.com/css2?family=Anton&family=Poppins:wght@600;700&family=Quicksand:wght@500&display=swap" rel="stylesheet">
<style>
  :root {
    --green-deep: #0f4d2b;
    --green-mid: #0b6a32;
    --green-bright: #049a2a;
    --red: #d4222d;
    --black: #000000;
    --white: #ffffff;
    --page: #ffffff;
    --ink-green: #1d5e34;
  }
  * { margin: 0; padding: 0; box-sizing: border-box; }
  html, body { width: 1200px; height: 1200px; overflow: hidden; background: var(--page); }
  .flyer {
    position: absolute; left: 266px; top: 127px;
    width: 668px; height: 932px; overflow: hidden; background: var(--white);
  }
  .flyer-inner {
    position: absolute; left: 0; top: 0; width: 1068px; height: 1492px;
    transform: scale(0.625); transform-origin: 0 0;
  }
  .shapes { position: absolute; left: 0; top: 0; }
  .brand {
    position: absolute; left: 360px; top: 112px; width: 400px; text-align: center;
    font-family: "Poppins", sans-serif; font-weight: 600; color: var(--ink-green);
    line-height: 1.05;
  }
  .brand-name { font-size: 72px; display: block; }
  .brand-sub { font-size: 22px; letter-spacing: 7px; display: block; margin-top: 4px; }
  .offer-bubble {
    position: absolute; left: 12px; top: 484px; width: 404px; height: 252px;
    border-radius: 30px; transform: rotate(-11deg);
    background: linear-gradient(135deg, var(--green-deep), var(--green-mid) 55%, var(--green-bright));
    display: flex; flex-direction: column; align-items: center; justify-content: center;
    font-family: "Anton", sans-serif; color: var(--white); line-height: 1.0; text-align: center;
  }
  .offer-line-1 { font-size: 52px; }
  .offer-line-2 { font-size: 62px; }
  .offer-line-3 { font-size: 88px; }
  .headline {
    position: absolute; left: 0; top: 798px; width: 1068px; text-align: center;
    color: var(--red); font-family: "Poppins", sans-serif; font-weight: 700; font-size: 45px;
  }
  .headline-accent {
    position: absolute; left: 0; top: 848px; width: 1068px; text-align: center;
    color: var(--red); font-family: "Anton", sans-serif; font-size: 68px; line-height: 1.1;
  }
  .feature-label {
    position: absolute; top: 1126px; width: 300px; text-align: center;
    color: var(--white); font-family: "Quicksand", sans-serif; font-weight: 500;
    font-size: 25px; line-height: 1.32;
  }
  .contact-button {
    position: absolute; left: 346px; top: 1202px; width: 392px; height: 74px;
    background: var(--red); border-radius: 26px;
    display: flex; align-items: center; justify-content: center;
    color: var(--white); font-family: "Poppins", sans-serif; font-weight: 700; font-size: 37px;
  }
  .contact-phone {
    position: absolute; left: 0; top: 1284px; width: 1068px; text-align: center;
    color: var(--white); font-family: "Poppins", sans-serif; font-weight: 700; font-size: 29px;
  }
  .address {
    position: absolute; top: 1377px; width: 320px; text-align: center;
    color: var(--white); font-family: "Poppins", sans-serif; font-weight: 700; font-size: 29px;
  }
</style>
</head>
<body>
<div class="flyer">
  <div class="flyer-inner">
    <svg class="shapes" width="1068" height="1492" viewBox="0 0 1068 1492">
      <defs>
        <linearGradient id="photoTone" x1="0" y1="0" x2="1" y2="1">
          <stop offset="0" stop-color="#c9c4bd"/>
          <stop offset="0.35" stop-color="#e4d3c4"/>
          <stop offset="0.65" stop-color="#d8dcd6"/>
          <stop offset="1" stop-color="#8a6a58"/>
        </linearGradient>
        <linearGradient id="swoosh" x1="0" y1="0" x2="1" y2="0">
          <stop offset="0" stop-color="#06a020"/>
          <stop offset="1" stop-color="#0a5a2e"/>
        </linearGradient>
        <linearGradient id="panel" x1="0" y1="0" x2="1" y2="0">
          <stop offset="0" stop-color="#134a2a"/>
          <stop offset="0.6" stop-color="#076a30"/>
          <stop offset="1" stop-color="#029c24"/>
        </linearGradient>
        <linearGradient id="ring" x1="0" y1="0" x2="1" y2="1">
          <stop offset="0" stop-color="#0f4d2b"/>
          <stop offset="1" stop-color="#06a020"/>
        </linearGradient>
      </defs>

      <path class="hero-photo" role="img" aria-label="Photo of two smiling women in a bright office"
            d="M0 0 H1068 V420 C900 650 650 720 360 705 L0 600 Z" fill="url(#photoTone)"/>

      <path class="swoosh-black" d="M330 705 C560 805 880 835 1068 667 V560 C860 740 600 770 330 705 Z" fill="var(--black)"/>
      <path class="swoosh-green" d="M350 705 C600 770 860 740 1068 570 V417 C900 650 650 720 350 705 Z" fill="url(#swoosh)"/>

      <ellipse cx="238" cy="780" rx="72" ry="9" fill="#d6d6d6"/>
      <polygon class="bubble-tail" points="190,740 290,728 245,762" fill="#11532c"/>

      <path class="footer-red" d="M0 1290 C80 1240 160 1212 230 1207 H880 C950 1207 1010 1212 1068 1215 V1492 H0 Z" fill="var(--red)"/>
      <path class="footer-black" d="M0 1340 C150 1250 280 1212 400 1207 H700 C850 1215 970 1250 1068 1302 V1492 H0 Z" fill="var(--black)"/>
      <path class="footer-dots" d="M3 1392 C120 1300 230 1250 333 1229 M745 1222 C880 1245 990 1300 1068 1372"
            fill="none" stroke="var(--white)" stroke-width="4" stroke-linecap="round" stroke-dasharray="0 15"/>

      <rect class="feature-panel" x="65" y="992" width="958" height="217" rx="32" fill="url(#panel)"/>
      <line x1="390" y1="1020" x2="390" y2="1200" stroke="#2d7a48" stroke-width="2" stroke-dasharray="2 6"/>
      <line x1="688" y1="1020" x2="688" y2="1200" stroke="#2d7a48" stroke-width="2" stroke-dasharray="2 6"/>

      <g class="feature-icon">
        <circle cx="214" cy="1019" r="92" fill="var(--white)"/>
        <circle cx="214" cy="1019" r="80" fill="var(--white)" stroke="url(#ring)" stroke-width="12"/>
        <g fill="none" stroke="var(--ink-green)" stroke-width="3" stroke-linecap="round">
          <circle cx="214" cy="1025" r="42"/>
          <circle cx="214" cy="1025" r="32"/>
          <rect x="204" y="953" width="20" height="12" rx="5"/>
          <line x1="214" y1="965" x2="214" y2="983"/>
          <line x1="176" y1="990" x2="168" y2="982"/>
          <line x1="252" y1="990" x2="260" y2="982"/>
          <path d="M222 1012 C214 1004 204 1010 208 1018 C212 1026 224 1024 222 1034 C218 1042 206 1038 204 1032"/>
          <line x1="213" y1="1000" x2="213" y2="1046"/>
        </g>
      </g>
      <g class="feature-icon">
        <circle cx="544" cy="1019" r="92" fill="var(--white)"/>
        <circle cx="544" cy="1019" r="80" fill="var(--white)" stroke="url(#ring)" stroke-width="12"/>
        <g fill="none" stroke="var(--ink-green)" stroke-width="3" stroke-linecap="round" stroke-linejoin="round">
          <path d="M520 1045 C495 1030 488 995 512 975 C535 958 570 965 578 990"/>
          <path d="M538 985 C532 980 522 983 524 991 C526 999 538 997 536 1005 C534 1012 524 1010 521 1005"/>
          <line x1="530" y1="975" x2="530" y2="1015"/>
          <path d="M550 1050 L542 1030 C538 1022 548 1018 552 1026 L556 1034 V996 C556 988 568 988 568 996 V1020 L586 1024 C596 1026 598 1034 596 1044 L590 1062 H560 Z"/>
        </g>
      </g>
      <g class="feature-icon">
        <circle cx="856" cy="1019" r="92" fill="var(--white)"/>
        <circle cx="856" cy="1019" r="80" fill="var(--white)" stroke="url(#ring)" stroke-width="12"/>
        <g fill="none" stroke="var(--ink-green)" stroke-width="3" stroke-linecap="round" stroke-linejoin="round">
          <rect x="840" y="955" width="50" height="96" rx="6"/>
          <line x1="855" y1="962" x2="875" y2="962"/>
          <path d="M808 1040 L830 1010 C836 1000 848 1000 852 1008 L862 1022 M816 1058 L830 1044 H860"/>
          <circle cx="864" cy="1008" r="14"/>
        </g>
      </g>
    </svg>

    <div class="brand"><span class="brand-name">Keystone</span><span class="brand-sub">LENDING GROUP</span></div>

    <div class="offer-bubble">
      <span class="offer-line-1">APPLY HER FOR</span>
      <span class="offer-line-2">$5.000-$6.000</span>
      <span class="offer-line-3">TODAY</span>
    </div>

    <p class="headline">File your taxes and apply for an</p>
    <p class="headline-accent">Easy Advance!</p>

    <p class="feature-label" style="left:64px">Available In<br>24 Hours or Less</p>
    <p class="feature-label" style="left:394px">Choose Your<br>Loan Amount</p>
    <p class="feature-label" style="left:706px">Quick and<br>Easy</p>

    <div class="contact-button">Contact Us Today!</div>
    <p class="contact-phone">Phone Number</p>
    <p class="address" style="left:58px">Address line 1</p>
    <p class="address" style="left:380px">Address line 2</p>
    <p class="address" style="left:698px">Address line 3</p>
  </div>
</div>
</body>
</html>
```